Melissa Dorvan Personal Business Card

I like orange. It's would better if my card have an orange background
Address: 5820 Halvers Lane #417
San Jose
California
US
Tel: 4085172049

Industry/Entity Type

Business

```html
<!DOCTYPE html>
<html lang="en">
<head>
<meta charset="utf-8">
<title>Melissa Dorvan — Business Card</title>
<link rel="stylesheet" href="https://fonts.googleapis.com/css2?family=Encode+Sans+Condensed:wght@500;600&display=swap">
<style>
  :root {
    --backdrop: #f2f2f2;
    --card-glow: #ffa000;
    --card-mid: #ff6a00;
    --card-edge: #ff2e05;
    --ink-white: #ffffff;
    --ink-depth: #cf1d00;
    --card-shadow: rgba(0, 0, 0, 0.18);
  }

  html, body {
    margin: 0;
    padding: 0;
    width: 1200px;
    height: 900px;
    overflow: hidden;
    background: var(--backdrop);
  }

  .canvas {
    position: relative;
    width: 1200px;
    height: 900px;
  }

  .business-card {
    position: absolute;
    left: 100px;
    top: 164px;
    width: 1000px;
    height: 572px;
    background: radial-gradient(ellipse 62% 70% at 46% 56%,
      var(--card-glow) 0%,
      var(--card-mid) 38%,
      var(--card-edge) 82%,
      var(--card-edge) 100%);
    box-shadow: 0 14px 40px var(--card-shadow);
  }

  .identity {
    position: absolute;
    left: 270px;
    top: 170px;
    font-family: "Encode Sans Condensed", sans-serif;
    color: var(--ink-white);
  }

  .identity__name {
    margin: 0;
    font-size: 150px;
    font-weight: 600;
    line-height: 1;
    letter-spacing: 1px;
    text-transform: lowercase;
    text-shadow:
      -1px 1px 0 var(--ink-depth),
      -2px 2px 0 var(--ink-depth),
      -3px 3px 0 var(--ink-depth),
      -4px 4px 0 var(--ink-depth),
      -5px 5px 0 var(--ink-depth),
      -6px 6px 0 var(--ink-depth);
  }

  .identity__contact {
    display: flex;
    gap: 30px;
    margin: 6px 0 0 10px;
    font-size: 19px;
    font-weight: 500;
    letter-spacing: 1px;
    white-space: nowrap;
    text-shadow:
      -1px 1px 0 var(--ink-depth),
      -2px 2px 0 var(--ink-depth);
  }
</style>
</head>
<body>
  <main class="canvas">
    <section class="business-card">
      <div class="identity">
        <h1 class="identity__name">melissa dorvan</h1>
        <p class="identity__contact">
          <span class="identity__street">5820 Halvers Lane #417</span>
          <span class="identity__city">San Jose</span>
          <span class="identity__state">California</span>
          <span class="identity__phone">Tel: 4085172049</span>
        </p>
      </div>
    </section>
  </main>
</body>
</html>
```